Silverpine Orbit Works Flyer

We need a one page promotional piece that explains what our company does, and the benefits it provides in a simple, elegant, easy to understand way. I would like to print it on glossy heavyweight paper to give a feel of high quality and legitimacy. I will include the logo, the tag line, and the main benefits that the company offers.

Tag line concept, may not need these exact words. "Lend us 5 minutes each morning, and we will guide you toward a Silverpine Orbit Works."

Key points...(exact wording not required if you think of a better way to say it)

Software easy enough for my grandpa to use.
Lets you use snail mail, email, texting, and social media to quickly market to your customers at very low cost.
Web based which allows you to launch media campaigns from your desktop, or smartphone in moments.
Quick 3 - 5 minute training videos which give you hard hitting, quick action tips that will help you make your business better today.
Live coaching calls to help motivate you to improve your business.
No contracts, or start up fees. One low price of $299 per month.

Restaurant owners

Restaurant

```html
<!DOCTYPE html>
<html lang="en">
<head>
<meta charset="utf-8">
<title>Silverpine Orbit Works Flyer</title>
<link rel="stylesheet" href="https://fonts.googleapis.com/css2?family=PT+Sans:wght@400;700&family=PT+Sans+Narrow:wght@700&display=swap">
<style>
  :root {
    --green-light: #d9ee9a;
    --green-mid: #9fd04a;
    --green-deep: #7cb631;
    --green-band: #6a9a2a;
    --green-text: #4f8a22;
    --blue-head: #0f5aa8;
    --blue-swoosh: #1d55a5;
    --red-top: #e0452b;
    --red-deep: #b3200f;
    --grey-dark: #565656;
    --grey-line: #6a6a6a;
    --grey-mark: #c9c9c9;
    --white: #ffffff;
  }
  html, body {
    margin: 0;
    padding: 0;
    width: 922px;
    height: 1200px;
    overflow: hidden;
    background: #ffffff;
  }
  .flyer {
    position: relative;
    width: 922px;
    height: 1200px;
    overflow: hidden;
    background:
      radial-gradient(ellipse 520px 460px at 300px 260px, rgba(255,255,255,0.85), rgba(255,255,255,0) 70%),
      linear-gradient(160deg, var(--green-light) 0%, var(--green-mid) 45%, var(--green-deep) 100%);
    font-family: "PT Sans", Arial, sans-serif;
  }
  .decor { position: absolute; left: 0; top: 0; }
  .brand {
    position: absolute;
    left: 110px;
    top: 70px;
    width: 330px;
    text-align: center;
  }
  .brand-mark {
    width: 170px;
    height: 170px;
    margin: 0 auto 26px;
    border-radius: 50%;
    background: var(--grey-mark);
  }
  .brand-name {
    margin: 0;
    font-family: "PT Sans Narrow", "Arial Narrow", sans-serif;
    font-weight: 700;
    font-size: 50px;
    line-height: 1.02;
    letter-spacing: 1px;
    text-transform: uppercase;
    color: var(--grey-dark);
  }
  .bubble {
    position: absolute;
    left: 462px;
    top: 120px;
    width: 430px;
    height: 200px;
    overflow: visible;
    z-index: 1;
  }
  .bubble-text {
    position: absolute;
    left: 527px;
    top: 160px;
    width: 300px;
    margin: 0;
    text-align: center;
    font-family: "PT Sans Narrow", "Arial Narrow", sans-serif;
    font-weight: 700;
    font-size: 36px;
    line-height: 40px;
    white-space: nowrap;
    color: var(--white);
    transform: rotate(-12deg);
    z-index: 2;
  }
  .headline {
    position: absolute;
    left: 80px;
    top: 470px;
    width: 800px;
    margin: 0;
    font-family: "PT Sans Narrow", "Arial Narrow", sans-serif;
    font-weight: 700;
    font-size: 56px;
    line-height: 64px;
    color: var(--blue-head);
  }
  .benefits {
    list-style: none;
    margin: 0;
    padding: 0;
  }
  .benefit {
    position: absolute;
    left: 58px;
    width: 780px;
    display: flex;
    align-items: stretch;
  }
  .benefit-num {
    position: relative;
    flex: 0 0 77px;
    display: flex;
    align-items: center;
    justify-content: center;
    background: linear-gradient(180deg, var(--red-top), var(--red-deep));
    color: var(--white);
    font-family: "PT Sans Narrow", "Arial Narrow", sans-serif;
    font-weight: 700;
    font-size: 50px;
    box-shadow: 2px 3px 5px rgba(0,0,0,0.3);
  }
  .benefit-num::before {
    content: "";
    position: absolute;
    left: 0;
    top: -10px;
    border-left: 12px solid transparent;
    border-bottom: 10px solid #7e1408;
  }
  .benefit-text {
    flex: 1;
    display: flex;
    align-items: center;
    padding: 0 14px;
    background: linear-gradient(90deg, #ffffff 70%, #eeeeee 100%);
    color: var(--green-text);
    font-size: 21px;
    line-height: 1.3;
    box-shadow: 2px 3px 5px rgba(0,0,0,0.25);
  }
  .b1 { top: 711px; height: 64px; }
  .b2 { top: 795px; height: 64px; }
  .b3 { top: 886px; height: 70px; }
  .b4 { top: 975px; height: 50px; }
  .b5 { top: 1043px; height: 48px; }
</style>
</head>
<body>
<main class="flyer">
  <svg class="decor" width="922" height="1200" viewBox="0 0 922 1200" aria-hidden="true">
    <path class="swoosh-top-red" d="M0 70 C 90 40, 200 15, 310 0 L 345 0 C 220 25, 100 65, 0 105 Z" fill="var(--red-top)"/>
    <path class="swoosh-top-grey" d="M0 140 C 120 80, 250 30, 380 0" stroke="var(--grey-line)" stroke-width="6" fill="none"/>
    <path class="swoosh-bottom-light" d="M420 1130 C 600 1090, 780 1040, 922 930 L 922 1060 C 780 1080, 620 1110, 420 1130 Z" fill="rgba(255,255,255,0.25)"/>
    <path class="swoosh-bottom-red" d="M150 1135 C 400 1110, 700 1085, 922 1040 L 922 1050 C 700 1095, 400 1122, 150 1135 Z" fill="var(--red-top)"/>
    <path class="swoosh-bottom-grey" d="M240 1150 C 480 1130, 720 1105, 922 1062" stroke="var(--grey-line)" stroke-width="5" fill="none"/>
    <path class="swoosh-bottom-blue" d="M320 1165 C 560 1150, 760 1120, 922 1078 L 922 1100 C 760 1140, 560 1162, 320 1165 Z" fill="var(--blue-swoosh)"/>
    <path class="bottom-band" d="M0 1160 C 300 1172, 650 1150, 922 1105 L 922 1200 L 0 1200 Z" fill="var(--green-band)"/>
  </svg>

  <header class="brand">
    <div class="brand-mark"></div>
    <p class="brand-name">Silverpine<br>Orbit Works</p>
  </header>

  <svg class="bubble" viewBox="0 0 430 200" aria-hidden="true">
    <g transform="rotate(-12 215 100)">
      <path d="M120 150 L 70 200 L 160 160 Z" fill="var(--grey-dark)" stroke="var(--white)" stroke-width="5"/>
      <ellipse cx="215" cy="100" rx="200" ry="82" fill="var(--grey-dark)" stroke="var(--white)" stroke-width="5"/>
      <path d="M122 152 L 86 188 L 158 158 Z" fill="var(--grey-dark)"/>
    </g>
  </svg>
  <p class="bubble-text">Software Easy<br>Enough for My<br>Grandpa to Use</p>

  <h1 class="headline">Lend us 5 minutes each morning,<br>and we will guide you toward a<br>Silverpine Orbit Works.</h1>

  <ol class="benefits">
    <li class="benefit b1"><span class="benefit-num">1</span><span class="benefit-text">Lets you use snail mail, email, texting, and social media to quickly market to your customers at very low cost.</span></li>
    <li class="benefit b2"><span class="benefit-num">2</span><span class="benefit-text">Web based which allows you to launch media campaigns from your desktop, or smartphone in moments.</span></li>
    <li class="benefit b3"><span class="benefit-num">3</span><span class="benefit-text">Quick 3 - 5 minute training videos which give you hard hitting, quick action tips that will help you make your business better today.</span></li>
    <li class="benefit b4"><span class="benefit-num">4</span><span class="benefit-text">Live coaching calls to help motivate you to improve your business</span></li>
    <li class="benefit b5"><span class="benefit-num">5</span><span class="benefit-text">No contracts, or start up fees. One low price of $299 per month.</span></li>
  </ol>
</main>
</body>
</html>
```